Flyer für Hausreinigung
Zielgruppe
Hausverwaltungen, Hausbesitzer.
Aufgabenstellung
Ergebnis soll ein Winword-Dokument mit einem Firmenlogo (Vorschlag: Tintenklecks hellgrün/blau verlaufend mit orangem Besen/Wischer/oder Hand - andere Ideen sind willkommen!) sein, das ich noch um Firmenname/Adresse bzw. Empfängerdaten noch vervollständigen/individualisieren kann. Es soll bunt, aber nicht überladen sein, eventuell mit Stockfotos von lachenden/glücklich schauenden aktiven Menschen sein, jung dynamisch aber nicht flippig. Folgender Text sollte darin vorkommen, Umformulierungen und andere Ideen sind hochwillkommen:
Unser Ziel ist es eine Hausbetreuung fast wie ein Hausbesorger zu leisten, jedoch mit zusätzlichen Vorteilen:
· Der Vertrag ist jederzeit ohne Frist kündbar, ohne Angabe von Gründen!
· Reinigung 1 x pro Woche sowie zusätzliche Bedarfsreinigung
· Krankheits- und Urlaubsvertretung sind bereits inklusive.
· Haftpflichtversicherung über 1,5 Mio. Euro
· Inklusive Gartenbetreuung, Garage, Dachboden, Haustechnik
· Kontrollgänge, 7 x 24 h Erreichbarkeit für Mieter und Eigentümer, Handwerkerüberwachung, Notfallkoordination
· Winterbetreuung der Gehsteige täglich mindestens zwischen 6:00 und 22:00
· Inklusive aller Hilfsmittel und Materialien
· Fixpreis pro Monat.
Nach Möglichkeit soll das auf 1 A4-Seite Platz finden.

```html
<!DOCTYPE html>
<html lang="de">
<head>
<meta charset="utf-8">
<title>Anton Brenner Hausbetreuung – Flyer</title>
<link rel="stylesheet" href="https://fonts.googleapis.com/css2?family=Open+Sans:wght@400;600;700;800&display=swap">
<style>
  :root {
    --green: #8cc63f;
    --ink: #3b3b3b;
    --ink-soft: #505050;
    --paper: #efeee9;
    --paper-light: #fbfbf8;
    --footer: #3a3a3a;
    --white: #ffffff;
    --concrete: #8e8d87;
    --concrete-dark: #5f5e59;
    --room-light: #ecebe6;
    --wall-dark: #3f3d39;
    --floor: #7a6a58;
  }
  * { margin: 0; padding: 0; box-sizing: border-box; }
  html, body { width: 848px; height: 1200px; overflow: hidden; }
  body { font-family: "Open Sans", Arial, sans-serif; color: var(--ink); }

  .flyer {
    position: relative;
    width: 848px; height: 1200px;
    overflow: hidden;
    background: linear-gradient(160deg, var(--paper-light) 0%, var(--paper) 60%, #e4e3dd 100%);
  }

  .dot { position: absolute; border-radius: 50%; background: var(--green); z-index: 3; }

  .interior-photo {
    position: absolute;
    left: 0; top: 590px;
    width: 848px; height: 527px;
    background:
      linear-gradient(180deg, rgba(239,238,233,1) 0%, rgba(239,238,233,0) 14%),
      linear-gradient(180deg, rgba(0,0,0,0) 72%, var(--floor) 100%),
      linear-gradient(90deg,
        var(--concrete) 0%, var(--concrete-dark) 20%, var(--concrete) 34%,
        var(--room-light) 44%, var(--white) 56%, var(--room-light) 64%,
        #6d6a64 74%, var(--wall-dark) 88%, #2f2d2a 100%);
  }

  .content {
    position: absolute;
    left: 190px; top: 55px;
    width: 700px;
    transform: rotate(9deg);
    transform-origin: 0 0;
    z-index: 2;
  }

  .brand {
    position: absolute; left: 150px; top: 0;
    display: flex; align-items: center; gap: 12px;
  }
  .brand-mark { width: 22px; height: 22px; background: var(--ink); }
  .brand-name {
    font-size: 46px; font-weight: 800; color: var(--ink);
    letter-spacing: -0.5px; line-height: 1;
  }

  .slogan-band {
    position: absolute; left: -20px; top: 66px;
    width: 760px; height: 48px;
    background: var(--green);
    display: flex; align-items: center;
    padding-left: 50px;
  }
  .slogan { font-size: 30px; font-weight: 800; color: var(--ink); }

  .intro {
    position: absolute; left: 40px; top: 132px; width: 590px;
    font-size: 19px; font-weight: 700; line-height: 1.27; color: var(--ink-soft);
  }

  .benefits {
    position: absolute; left: 10px; top: 226px; width: 650px;
    list-style: none;
    font-size: 14.5px; line-height: 1.3; color: var(--ink-soft);
  }
  .benefits li { position: relative; padding-left: 20px; margin-bottom: 10px; }
  .benefits li::before {
    content: ""; position: absolute; left: 0; top: 4px;
    width: 9px; height: 9px; border-radius: 50%; background: var(--green);
  }

  .contact-bar {
    position: absolute; left: 0; bottom: 0;
    width: 848px; height: 83px;
    background: var(--footer);
    color: var(--white);
    text-align: center;
    padding-top: 14px;
  }
  .contact-call { font-size: 21px; font-weight: 700; }
  .contact-details { font-size: 14px; font-weight: 600; margin-top: 6px; color: #e8e8e8; }
</style>
</head>
<body>
<div class="flyer">

  <span class="dot" style="left:46px; top:120px; width:70px; height:70px;"></span>
  <span class="dot" style="left:16px; top:200px; width:14px; height:14px;"></span>
  <span class="dot" style="left:702px; top:6px; width:64px; height:64px;"></span>
  <span class="dot" style="left:662px; top:30px; width:14px; height:14px;"></span>
  <span class="dot" style="left:118px; top:1090px; width:52px; height:52px;"></span>

  <div class="interior-photo" role="img" aria-label="Foto eines modernen, hellen Wohnraums mit Betonwand, schwebender Holztreppe, weißem Sofa und Bogenleuchte"></div>

  <div class="content">
    <div class="brand">
      <span class="brand-mark"></span>
      <span class="brand-name">ANTON BRENNER</span>
    </div>

    <div class="slogan-band">
      <h1 class="slogan">Rund um´s Haus aus einer Hand!</h1>
    </div>

    <p class="intro">Wir bieten Ihnen den kompletten Service rundum Ihr Haus. Überzeugen Sie sich von unserem umfangreichen Service und profitieren Sie von zusätzlichen Vorteilen:</p>

    <ul class="benefits">
      <li>Ihr Vertrag ist jederzeit ohne Frist kündbar und das sogar ohne Angabe von Gründen!</li>
      <li>Gründliche Reinigung 1 x pro Woche sowie zusätzliche Bedarfsreinigung nach Vereinbarung.</li>
      <li>Krankheits- und Urlaubsvertretung sind bereits inklusive.</li>
      <li>Umfangreiche Haftpflichtversicherung über 1,5 Mio. Euro.</li>
      <li>Inklusive Garten-, Dachboden-, Garage-, Haustechnikbetreuung und vielen mehr.</li>
      <li>Eigenständige Kontrollgänge, 7x24 h Erreichbarkeit für Mieter und Eigentümer, Handwerker-überwachung und Notfallkoordination.</li>
      <li>Winterbetreuung der Gehsteige täglich mindestens zwischen 6:00 und 22:00 Uhr</li>
      <li>Hilfsmittel und Materialien sind bei allen Vereinbarungen inklusive.</li>
      <li>Das alles zum einem sorglosen monatlichen Top Fixpreis für Sie.</li>
    </ul>
  </div>

  <footer class="contact-bar">
    <p class="contact-call">Wir freuen uns auf Ihren Anruf:</p>
    <p class="contact-details">Anton Brenner Hausbetreuung | Lindenweg 8 | 54321 Feldheim | Tel. 06543/98765432</p>
  </footer>

</div>
</body>
</html>
```